NZ First of it's kind solutions directory and marketplace for busy Mums needs a business card design

We need a business card design for our new nationwide business in NZ (long term plans to go global). We provide solutions to the everyday challenges that busy Mums face by connecting them with quality communities and suppliers of carefully selected, relevant products and services. We sell direct via our online marketplace. The final design should communicate our values of inclusivity, quality and smart solutions. Colours should incorporate our logo colour palette of #477077 and #6ba8b2. Our website is at https://www.brightnestly.com

Target Market(s)

busy Mums, Age 28 – 50, female, income over $100K, location main centres NZ primarily but NZ wide. Is likely juggling work or career with a young family. Probably had hobbies which have fallen by the wayside.
-Wants to succeed in her chosen career without compromising on family life
-to successfully juggle her career without feeling like she is compromising her children
- Is time poor, something always has to give and it’s generally her health (she’ll stay up late, get stressed)
- probably ex corporate or professional career. Has discretional income

Industry/Entity Type

Business

Contact Information for Business Card

Jodie Farnsworth, Founder, BrightNestly.com (Strapline Browse; Pick; Sorted), 48 Kowhai Terrace, Hillsborough, Auckland 1058, New Zealand. Mob: 021 437 518 Ph: +64 (0)9 584 7163

Font styles to use
Other font styles liked:
• Raleway, and/or Architects Daughter

Colors
00a990
33b8a4
86cfc6
cfeae6

Requirements
Must have
• the above details, streamline. the logo and colours associated with those logos
Should not have
• foil or metallic colours

```html
<!DOCTYPE html>
<html lang="en">
<head>
<meta charset="utf-8">
<title>BrightNestly Business Card</title>
<link href="https://fonts.googleapis.com/css2?family=Raleway:wght@400;500;700;800&display=swap" rel="stylesheet">
<style>
  :root {
    --backdrop: #00a990;
    --card: #d2eae6;
    --brand-dark: #477077;
    --brand-light: #6ba8b2;
    --accent: #00a990;
    --ink: #1f2a2c;
    --icon: #3d4547;
  }
  * { margin: 0; padding: 0; box-sizing: border-box; }
  html, body {
    width: 1200px; height: 1200px; overflow: hidden;
    background: var(--backdrop);
    font-family: "Raleway", Arial, sans-serif;
  }
  .canvas { position: relative; width: 1200px; height: 1200px; }
  .card {
    position: absolute; left: 180px; width: 840px; height: 480px;
    background: var(--card);
  }
  .card--front { top: 86px; }
  .card--back { top: 634px; }

  .brand { position: absolute; display: flex; align-items: center; white-space: nowrap; }
  .brand__dot { border-radius: 50%; background: var(--brand-dark); flex: none; }
  .brand__name { font-weight: 800; color: var(--brand-dark); letter-spacing: -0.02em; }

  .card--front .brand { left: 192px; top: 186px; }
  .card--front .brand__dot { width: 56px; height: 56px; margin-right: 22px; }
  .card--front .brand__name { font-size: 62px; line-height: 1; }
  .front-url {
    position: absolute; right: 192px; top: 290px;
    font-size: 16px; letter-spacing: 0.32em; color: var(--ink);
  }

  .card--back .brand { left: 38px; top: 88px; }
  .card--back .brand__dot { width: 36px; height: 36px; margin-right: 14px; }
  .card--back .brand__name { font-size: 36px; line-height: 1; }

  .person { position: absolute; right: 40px; top: 250px; text-align: right; }
  .person__name { font-size: 30px; color: var(--accent); line-height: 1.1; }
  .person__role { font-size: 24px; color: var(--ink); line-height: 1.15; }
  .divider {
    position: absolute; left: 38px; width: 765px; top: 311px;
    height: 2px; background: var(--accent);
  }

  .contacts { position: absolute; left: 52px; top: 350px; list-style: none; }
  .contacts li {
    display: flex; align-items: center; height: 27.3px;
    font-size: 17px; color: var(--ink);
  }
  .contacts svg { width: 18px; height: 18px; margin-right: 13px; fill: var(--icon); flex: none; }

  .address {
    position: absolute; right: 38px; top: 407px; text-align: right;
    font-size: 17px; line-height: 24px; color: var(--ink); font-style: normal;
  }
</style>
</head>
<body>
<main class="canvas">
  <section class="card card--front">
    <div class="brand">
      <span class="brand__dot"></span>
      <span class="brand__name">BrightNestly</span>
    </div>
    <p class="front-url">brightnestly.com</p>
  </section>

  <section class="card card--back">
    <div class="brand">
      <span class="brand__dot"></span>
      <span class="brand__name">BrightNestly</span>
    </div>

    <div class="person">
      <p class="person__name">Jodie Farnsworth</p>
      <p class="person__role">Funder</p>
    </div>
    <div class="divider"></div>

    <ul class="contacts">
      <li>
        <svg viewBox="0 0 24 24" aria-hidden="true"><path d="M6.6 10.8a15.1 15.1 0 0 0 6.6 6.6l2.2-2.2a1 1 0 0 1 1-.25 11.4 11.4 0 0 0 3.6.57 1 1 0 0 1 1 1V20a1 1 0 0 1-1 1A17 17 0 0 1 3 4a1 1 0 0 1 1-1h3.5a1 1 0 0 1 1 1c0 1.25.2 2.45.57 3.57a1 1 0 0 1-.25 1z"/></svg>
        021 437 518
      </li>
      <li>
        <svg viewBox="0 0 24 24" aria-hidden="true"><path d="M2 9c0-2 4.5-4 10-4s10 2 10 4v1.5h-5V8.5H7v2H2z"/><path d="M6 11h12l2 8H4z"/><circle cx="12" cy="15" r="2" fill="#d2eae6"/></svg>
        +64 (0)9 584 7163
      </li>
      <li>
        <svg viewBox="0 0 24 24" aria-hidden="true"><path d="M2 5h20v14H2z"/><path d="M2.5 5.5 12 13l9.5-7.5" fill="none" stroke="#d2eae6" stroke-width="1.6"/></svg>
        @brightnestly.com
      </li>
      <li>
        <svg viewBox="0 0 24 24" aria-hidden="true" fill="none" stroke="#3d4547" stroke-width="1.4" style="fill:none"><circle cx="12" cy="12" r="9.5"/><ellipse cx="12" cy="12" rx="4.5" ry="9.5"/><path d="M2.5 12h19M4 7h16M4 17h16M12 2.5v19"/></svg>
        brightnestly.com
      </li>
    </ul>

    <address class="address">
      48 Kowhai Terrace, Hillsborough,<br>
      Auckland 1058, Newzeland
    </address>
  </section>
</main>
</body>
</html>
```